A simple Facebook Ad (not Facebook Page) for weight loss surgery

It’s a simple ad in terms of the text.

The text should say:
Curious about weight loss surgery?
This 30 second quiz will tell you which procedure will suit you best

I'm open to variations in the text if it is thought to enhance the ad.

Targeted towards obese individuals who have been unable to lose weight with diet and exercise. My industry is weight loss surgery – webpage www.merivalebardsley.com.au. Clicking the ad leads to a quiz on my webpage relating to weight loss surgery. Most frequent users of this service are females (75%) between ages of 35 and 55 years.

Successful weight loss surgery can enable individuals who have been unable to lose weight to lose a substantial amount of the excess weight they are carrying to be healthier and happier.

```html
<!DOCTYPE html>
<html lang="en">
<head>
<meta charset="utf-8">
<title>Weight Loss Surgery Quiz Ad</title>
<link rel="stylesheet" href="https://fonts.googleapis.com/css2?family=Poppins:wght@600;700;800&display=swap">
<style>
  :root {
    --teal: #137f74;
    --teal-soft: #7fc9c2;
    --ink: #121a1f;
    --paper: #ffffff;
    --stage: #f2f4f5;
    --rule: #3a3f42;
    --skin: #d9a98a;
  }
  html, body {
    margin: 0;
    padding: 0;
    width: 1200px;
    height: 2400px;
    overflow: hidden;
    background: var(--stage);
    font-family: "Poppins", sans-serif;
  }
  .ad {
    position: absolute;
    left: 0;
    top: 600px;
    width: 1200px;
    height: 1200px;
    background: var(--paper);
    overflow: hidden;
  }
  .ad-photo {
    position: absolute;
    left: 0;
    top: 245px;
    width: 450px;
    height: 955px;
    background: linear-gradient(180deg, #c89a7f 0%, var(--skin) 30%, #9fd8d2 60%, #2f3437 78%, var(--teal-soft) 100%);
    opacity: 0.85;
  }
  .headline {
    position: absolute;
    left: 310px;
    top: 70px;
    margin: 0;
    font-weight: 800;
    font-size: 118px;
    line-height: 110px;
    letter-spacing: -1px;
    color: var(--ink);
    text-transform: uppercase;
  }
  .headline .accent { color: var(--teal); }
  .quiz-band {
    position: absolute;
    left: 258px;
    top: 547px;
    width: 942px;
    height: 130px;
    background: var(--teal);
    color: var(--paper);
    box-sizing: border-box;
    padding: 8px 0 0 68px;
    font-weight: 700;
    font-size: 43px;
    line-height: 50px;
    display: flex;
    align-items: center;
  }
  .contact {
    position: absolute;
    left: 516px;
    top: 716px;
    right: 0;
  }
  .contact-title {
    margin: 0;
    font-weight: 800;
    font-size: 56px;
    line-height: 60px;
    color: var(--ink);
    text-transform: uppercase;
  }
  .contact-title .accent { color: var(--teal); }
  .contact-rule {
    margin: 22px 0 0;
    border: 0;
    border-top: 2px solid var(--rule);
  }
  .contact-line {
    display: flex;
    align-items: center;
    gap: 20px;
    color: var(--ink);
    font-weight: 800;
  }
  .contact-line svg { flex: none; }
  .phone { font-size: 68px; line-height: 80px; margin-top: 10px; }
  .web { font-size: 36px; line-height: 46px; font-weight: 700; }
  .brand {
    display: flex;
    align-items: center;
    gap: 18px;
    margin-top: 48px;
  }
  .brand-dot {
    width: 64px;
    height: 64px;
    border-radius: 50%;
    background: var(--teal);
  }
  .brand-text {
    color: var(--teal);
    font-weight: 600;
    font-size: 44px;
    line-height: 46px;
    text-transform: uppercase;
    letter-spacing: 1px;
  }
  .brand-text small {
    display: block;
    font-size: 15px;
    line-height: 20px;
    letter-spacing: 2.5px;
  }
</style>
</head>
<body>
  <main class="ad">
    <div class="ad-photo" role="img" aria-label="Smiling woman in teal activewear holding a bathroom scale"></div>

    <h1 class="headline">
      <span class="accent">Curious</span><br>
      <span class="accent">About</span><br>
      <span class="accent">Weight</span> Loss<br>
      Surgery?
    </h1>

    <div class="quiz-band">This 30 second quiz will tell you which<br>procedure will suit you best</div>

    <section class="contact">
      <h2 class="contact-title">Contact us for<br><span class="accent">all appointments</span></h2>
      <hr class="contact-rule">
      <div class="contact-line phone">
        <svg width="46" height="46" viewBox="0 0 24 24" aria-hidden="true">
          <path d="M6.6 10.8a15 15 0 0 0 6.6 6.6l2.2-2.2a1 1 0 0 1 1-.25 11.4 11.4 0 0 0 3.6.6 1 1 0 0 1 1 1V20a1 1 0 0 1-1 1A17 17 0 0 1 3 4a1 1 0 0 1 1-1h3.5a1 1 0 0 1 1 1c0 1.25.2 2.45.6 3.6a1 1 0 0 1-.25 1z" fill="var(--teal)"/>
          <path d="M14 3a7 7 0 0 1 7 7M14 6.5a3.5 3.5 0 0 1 3.5 3.5" stroke="var(--teal)" stroke-width="1.8" fill="none" stroke-linecap="round"/>
        </svg>
        <span>03 9000 4127</span>
      </div>
      <div class="contact-line web">
        <svg width="46" height="46" viewBox="0 0 24 24" aria-hidden="true">
          <g fill="none" stroke="var(--teal)" stroke-width="1.8">
            <circle cx="12" cy="12" r="10"/>
            <ellipse cx="12" cy="12" rx="4.5" ry="10"/>
            <path d="M2 12h20M4 7h16M4 17h16"/>
          </g>
        </svg>
        <span>www.merivalebardsley.com.au</span>
      </div>
      <div class="brand">
        <div class="brand-dot"></div>
        <div class="brand-text">Merivale Bardsley<small>General, Upper GI &amp; Bariatric Surgeon</small></div>
      </div>
    </section>
  </main>
</body>
</html>
```